Business Card Design Project

We consult with hotels on setting rates and maximizing a revenue strategy

Industry/Entity Type

Business

Contact Information for Business Card

I am not sure what I want. Our company offers high level consulting to hotels around the country but we are also laid back. I would like something that is professional but also shows the laid back side

```html
<!DOCTYPE html>
<html lang="en">
<head>
<meta charset="utf-8">
<title>Harborline – Business Card</title>
<link rel="stylesheet" href="https://fonts.googleapis.com/css2?family=Barlow:wght@400;600&display=swap">
<style>
  :root {
    --backdrop: #8a7c70;
    --card-white: #fbfbfa;
    --brand-teal: #2b7e77;
    --ink-dark: #2e2623;
    --ink-light: #ffffff;
  }
  html, body {
    margin: 0;
    padding: 0;
    width: 1200px;
    height: 899px;
    overflow: hidden;
    background: var(--backdrop);
    font-family: "Barlow", Arial, sans-serif;
  }
  .canvas {
    position: relative;
    width: 1200px;
    height: 899px;
  }
  .business-card {
    position: absolute;
    left: 150px;
    top: 185px;
    width: 900px;
    height: 530px;
    display: flex;
    box-shadow: 0 6px 18px rgba(0, 0, 0, 0.25);
  }
  .brand-side {
    width: 440px;
    background: var(--card-white);
    position: relative;
  }
  .brand-name {
    position: absolute;
    left: 62px;
    top: 178px;
    display: flex;
    align-items: center;
    gap: 14px;
    color: var(--brand-teal);
    font-weight: 600;
    font-size: 44px;
    letter-spacing: 1px;
  }
  .brand-mark {
    width: 30px;
    height: 30px;
    background: var(--brand-teal);
  }
  .website {
    position: absolute;
    left: 58px;
    top: 290px;
    color: var(--ink-dark);
    font-size: 29px;
    font-weight: 400;
  }
  .contact-side {
    flex: 1;
    background: var(--brand-teal);
    color: var(--ink-light);
    padding: 205px 0 0 24px;
    box-sizing: border-box;
  }
  .person-name,
  .person-title {
    margin: 0;
    font-weight: 600;
    font-size: 28px;
    line-height: 36px;
  }
  .person-name { text-transform: uppercase; letter-spacing: 0.5px; }
  .contact-list {
    list-style: none;
    margin: 40px 0 0;
    padding: 0;
    font-size: 27px;
    line-height: 37px;
    font-weight: 400;
  }
</style>
</head>
<body>
  <main class="canvas">
    <article class="business-card">
      <section class="brand-side">
        <div class="brand-name"><span class="brand-mark"></span>HARBORLINE</div>
        <div class="website">www.HarborlineRMS.com</div>
      </section>
      <section class="contact-side">
        <h1 class="person-name">Nora Whitfield</h1>
        <p class="person-title">Regional Revenue Manager</p>
        <ul class="contact-list">
          <li>Office 555-310-4821</li>
          <li>Fax 555-310-4830</li>
          <li>Nora@HarborlineRMS.com</li>
        </ul>
      </section>
    </article>
  </main>
</body>
</html>
```